Upbeat Accouting Package Flyer

I am looking for a 1 page (front, or front and back) flyer that will become our marketing for our accounting services. We are looking for something a little different and we are catering to the small retail shop owners. We have 3 accounting packages we would like to display and then some add-ons. I have included our logo that must be included in the design. I have uploaded the accounting package information as well.
Target Market(s)
Small Retail Shop Owners
Industry/Entity Type
Accounting
Colors
Designer to choose colors to be used in the design.
Requirements
Must have
- A casual feel. We are not your typical accountants who are very professional and "stuffy". I want it to feel like we are all family.
Nice to have
- I would like to incorporate some sort of retail theme.
- We have a couple of taglines we like to use and it would be great if they could be included. They are "We know you CAN do the accounting, but do you WANT to?" and "We allow you to get back to what's important."
Should not have
- Typical stock accounting photos of people shaking hands, large office buildings, etc.

```html
<!DOCTYPE html>
<html lang="en">
<head>
<meta charset="utf-8">
<title>Brightwell Tax and Accounting – Accounting Packages Flyer</title>
<link href="https://fonts.googleapis.com/css2?family=Source+Sans+3:wght@400;600;700&display=swap" rel="stylesheet">
<style>
  :root{
    --cyan:#2bb5e2;
    --teal:#1b8f98;
    --teal-deep:#16616a;
    --ink:#1f1f22;
    --dark:#3a3b3e;
    --white:#ffffff;
    --backdrop:#c9c9c9;
  }
  *{box-sizing:border-box;margin:0;padding:0}
  html,body{width:1200px;height:2250px;overflow:hidden}
  body{background:var(--backdrop);font-family:"Source Sans 3",sans-serif;color:var(--ink)}
  .flyer{position:absolute;left:100px;top:418px;width:1000px;height:1414px;background:var(--white);overflow:hidden;box-shadow:0 10px 30px rgba(0,0,0,.25)}

  /* hero */
  .hero-photo{position:absolute;left:0;top:0;width:1000px;height:549px;
    background:linear-gradient(100deg,#5d7f8a 0%,#9fb2bb 35%,#f4f6f7 55%,#cfd9e0 70%,#8da2b2 100%)}
  .hero-panel{position:absolute;left:0;top:0;width:429px;height:549px;background:rgba(27,143,152,.82)}
  .brand{position:absolute;left:52px;top:70px;width:340px;color:var(--white);font-weight:600;font-size:34px;line-height:40px}
  .headline{position:absolute;left:14px;top:196px;width:420px;text-align:center;color:var(--white);font-weight:700;font-size:52px;line-height:64px}
  .headline .caps{font-variant:small-caps}

  /* packages */
  .tag{position:absolute;background:var(--cyan);color:var(--white);font-weight:600;text-transform:uppercase;
    clip-path:polygon(14px 0,calc(100% - 14px) 0,100% 50%,calc(100% - 14px) 100%,14px 100%,0 50%);
    display:flex;align-items:center;justify-content:center}
  .tag-main{left:283px;top:571px;width:435px;height:42px;font-size:27px}
  .tag-sm{height:32px;font-size:21px;padding:0 22px}
  .package{position:absolute}
  .package ul{list-style:none;margin-top:12px}
  .package li{position:relative;padding-left:24px;font-size:17.5px;font-weight:600;line-height:23.5px}
  .package li::before{content:"";position:absolute;left:4px;top:5px;width:6px;height:11px;
    border-right:2px solid var(--ink);border-bottom:2px solid var(--ink);transform:rotate(45deg)}
  .package .tag{position:static;display:inline-flex}
  .pkg-develop{left:39px;top:646px;width:450px}
  .pkg-grow{left:39px;top:852px;width:450px}
  .pkg-relax{left:508px;top:646px;width:470px}
  .pkg-options{left:508px;top:976px;width:470px}
  .indent{padding-left:68px;display:block}

  /* footer */
  .footer-art{position:absolute;left:0;top:1160px;width:1000px;height:254px}
  .contact{position:absolute;left:39px;top:1240px;color:var(--white);font-size:16.5px;line-height:23px}
  .contact-title{color:var(--cyan);font-weight:700;font-size:17px;margin-bottom:4px;text-transform:uppercase}
  .contact li{list-style:none;display:flex;align-items:center;gap:10px;padding-left:2px}
  .contact svg{width:13px;height:13px;flex:none}
  .social{position:absolute;left:604px;top:1322px;color:var(--white);font-weight:700;font-size:16px}
  .social-icons{display:flex;gap:10px;margin-top:8px}
  .social-icons span{width:28px;height:28px;background:var(--white);border-radius:3px}
</style>
</head>
<body>
<main class="flyer">
  <section class="hero">
    <div class="hero-photo" role="img" aria-label="Photo of a cheerful team giving high fives in a bright office"></div>
    <div class="hero-panel"></div>
    <div class="brand">Brightwell Tax and Accounting Inc.</div>
    <h1 class="headline">We know you<br>CAN do the<br><span class="caps">Accounting</span>,<br>but do you<br>WANT to?</h1>
  </section>

  <div class="tag tag-main">Accounting Packages:</div>

  <section class="package pkg-develop">
    <div class="tag tag-sm">Develop:</div>
    <ul>
      <li>$300/mo when paid annually $325/mo billed monthly</li>
      <li>LedgerLite Online subscription</li>
      <li>Free accounting setup</li>
      <li>Weekly transaction processing</li>
      <li>Monthly account reconciliation (up to 2 accounts)</li>
      <li>Monthly financial statements by the 15th of the month</li>
    </ul>
  </section>

  <section class="package pkg-grow">
    <div class="tag tag-sm">Grow:</div>
    <ul>
      <li>$550/mo billed annually; $575/mo billed monthly</li>
      <li>LedgerLite Online subscription</li>
      <li>Free accounting setup</li>
      <li>Weekly transaction processing</li>
      <li>Monthly account reconciliation (up to 4 accounts)</li>
      <li>Monthly financial statements by the 10th of the month</li>
      <li>Client portal access for document sharing</li>
      <li>1 Custom Report</li>
      <li>Accounts Payable</li>
      <li>Monthly Scorecard (customized metric tracking<br>for your business)</li>
    </ul>
  </section>

  <section class="package pkg-relax">
    <div class="tag tag-sm">Relax (We’ve got this):</div>
    <ul>
      <li>$850/mo billed annually; $875/mo billed monthly</li>
      <li>LedgerLite Online subscription</li>
      <li>Free accounting setup</li>
      <li>Weekly transaction processing</li>
      <li>Monthly account reconciliation (up to 5-10 accounts)</li>
      <li>Monthly financial statements by the 5th of the month</li>
      <li>Client portal access for document sharing</li>
      <li>2 Custom Reports</li>
      <li>Accounts Payable</li>
      <li>Invoicing and accounts receivable</li>
      <li>Weekly Scorecard (customized metric tracking<br>for your business)</li>
    </ul>
  </section>

  <section class="package pkg-options">
    <div class="tag tag-sm">Additional Options</div>
    <ul>
      <li>Payroll – 1-10 employees $85/mo<span class="indent">11-30 employees $175/mo</span></li>
      <li>Sales tax - $30/mo per state</li>
      <li>Corporate taxes $50/mo</li>
      <li>Owner taxes - $25/mo</li>
    </ul>
  </section>

  <footer>
    <svg class="footer-art" viewBox="0 0 1000 254" preserveAspectRatio="none">
      <polygon points="0,60 1000,0 1000,254 0,254" fill="var(--dark)"/>
      <polygon role="img" aria-label="Photo of a desk with a calculator and pen" points="480,30 1000,0 1000,254 330,254" fill="var(--teal)"/>
      <polygon points="560,25 1000,0 1000,34 620,60" fill="var(--teal-deep)" opacity=".55"/>
      <polygon points="150,254 330,182 560,142 420,254" fill="var(--cyan)"/>
      <polygon points="560,142 700,104 610,182 420,254" fill="var(--cyan)" opacity=".55"/>
    </svg>
    <div class="contact">
      <div class="contact-title">Brightwell Tax and Accounting Inc.</div>
      <ul>
        <li><svg viewBox="0 0 12 12"><path d="M6 1a3.5 3.5 0 0 0-3.5 3.5C2.5 7.5 6 11 6 11s3.5-3.5 3.5-6.5A3.5 3.5 0 0 0 6 1z" fill="none" stroke="#fff" stroke-width="1.2"/><circle cx="6" cy="4.5" r="1.2" fill="#fff"/></svg>4512 W. 61st Street</li>
        <li><svg viewBox="0 0 12 12"></svg>Maplewood, KS 66000</li>
        <li><svg viewBox="0 0 12 12"><path d="M3 1.5l2 2-1 1.5c.7 1.3 1.7 2.3 3 3l1.5-1 2 2-1.5 1.5C5.5 10.5 1.5 6.5 1.5 3z" fill="#fff"/></svg>(555) 014-2290</li>
        <li><svg viewBox="0 0 12 12"><rect x="1" y="2.5" width="10" height="7" fill="none" stroke="#fff" stroke-width="1.2"/><path d="M1 2.5l5 4 5-4" fill="none" stroke="#fff" stroke-width="1.2"/></svg>accounting@brightwell-books.com</li>
        <li><svg viewBox="0 0 12 12"><circle cx="6" cy="6" r="5" fill="none" stroke="#fff" stroke-width="1.2"/><path d="M1 6h10M6 1c-2 2.5-2 7.5 0 10M6 1c2 2.5 2 7.5 0 10" fill="none" stroke="#fff" stroke-width="1"/></svg>www.brightwellbooks.com</li>
      </ul>
    </div>
    <div class="social">
      SOCIAL MEDIA
      <div class="social-icons"><span></span><span></span><span></span><span></span></div>
    </div>
  </footer>
</main>
</body>
</html>
```